Family Ranch with a hobby vineyard needs 2 wine labels for our first harvest

Design 2 wine labels (front and back) with the Brindor Ranch logo.
Label 1:
Sauvignon Blanc
Alc. 12.5% by Vol.
Palos Verdes Peninsula - add as the region
Year 2022
Label 2:
Cabernet Sauvignon
Alc. 13.5% by Vol.
Year 2022
For the back label design:
GOVERNMENT WARNING: (1) According to the Surgeon General, women
should not drink alcoholic beverages during pregnancy because of the risk of
birth defects. (2) Consumption of alcoholic beverages impairs your ability to
drive a car or operate machinery, and may cause health problems.
Contains Sulfates.
750ML
I just received the bottles and have attached a picture.
Look and feel
Each slider illustrates characteristics of the customer's brand and the style your logo design should communicate.

```html
<!DOCTYPE html>
<html lang="en">
<head>
<meta charset="utf-8">
<title>Brindor Ranch Wine Labels</title>
<link href="https://fonts.googleapis.com/css2?family=Marcellus+SC&family=Josefin+Sans:wght@600&display=swap" rel="stylesheet">
<style>
  :root {
    --backdrop: #a9a9a9;
    --paper: #ffffff;
    --gold: #c8b07f;
    --gold-band: #d8c49b;
    --maroon: #7b0d26;
    --ink: #2a2a2a;
    --text-grey: #5a5a5a;
    --shadow: rgba(0, 0, 0, 0.35);
  }
  * { margin: 0; padding: 0; box-sizing: border-box; }
  html, body { width: 1200px; height: 1000px; overflow: hidden; }
  body {
    background: var(--backdrop);
    font-family: "Marcellus SC", serif;
    position: relative;
  }
  .label {
    position: absolute;
    width: 387px;
    height: 387px;
    background: var(--paper);
    box-shadow: 0 14px 30px var(--shadow);
    overflow: hidden;
  }
  .front--blanc { left: 188px; top: 91px; }
  .back--blanc  { left: 626px; top: 92px; border: 7px solid var(--gold-band); }
  .front--cab   { left: 188px; top: 539px; }
  .back--cab    { left: 628px; top: 541px; border: 8px solid var(--maroon); }

  .front__scene {
    height: 249px;
    background:
      linear-gradient(180deg, #9fc6d6 0%, #e8b596 22%, #f0a877 32%, transparent 45%),
      linear-gradient(100deg, #c75a26 0%, #d77a3a 35%, #7aa24a 55%, #8fb3bf 70%, #5d8aa1 100%);
  }
  .front__info {
    text-align: center;
    padding-top: 14px;
  }
  .brand-name {
    font-family: "Marcellus SC", serif;
    color: var(--text-grey);
    font-size: 12px;
    letter-spacing: 1px;
    line-height: 1;
  }
  .wine-name {
    font-size: 27px;
    letter-spacing: 1.5px;
    line-height: 1;
    margin-top: 8px;
  }
  .front--blanc .wine-name { color: var(--gold); }
  .front--cab .wine-name   { color: var(--maroon); }
  .abv {
    font-size: 8px;
    color: var(--text-grey);
    margin-top: 7px;
  }
  .region {
    font-size: 12px;
    color: var(--ink);
    letter-spacing: 0.8px;
    margin-top: 4px;
  }
  .vintage {
    font-size: 7px;
    color: var(--text-grey);
    letter-spacing: 1px;
    margin-top: 12px;
  }
  .front__band {
    position: absolute;
    left: 0; right: 0; bottom: 0;
    height: 13px;
  }
  .front--blanc .front__band { background: var(--gold-band); }
  .front--cab .front__band   { background: var(--maroon); }

  .back__content {
    text-align: center;
    color: var(--text-grey);
    padding-top: 22px;
  }
  .warning-title {
    font-family: "Josefin Sans", sans-serif;
    font-weight: 600;
    color: var(--ink);
    font-size: 13px;
    letter-spacing: 4px;
  }
  .warning-text {
    font-size: 12px;
    line-height: 16px;
    margin-top: 20px;
    padding: 0 24px;
  }
  .warning-text + .warning-text { margin-top: 14px; }
  .sulfites { font-size: 12px; margin-top: 17px; }
  .volume { font-size: 13px; margin-top: 14px; color: var(--ink); }
  .back-brand {
    margin-top: 24px;
    display: inline-flex;
    align-items: center;
    gap: 7px;
    font-size: 15px;
    color: var(--ink);
    letter-spacing: 1px;
  }
  .back-brand__dot {
    width: 11px; height: 11px;
    border-radius: 50%;
    background: var(--ink);
  }
</style>
</head>
<body>

  <section class="label front front--blanc">
    <div class="front__scene" role="img" aria-label="Photograph of a lighthouse with palm trees on red coastal cliffs above the ocean at sunset"></div>
    <div class="front__info">
      <p class="brand-name">Brindor Ranch</p>
      <h2 class="wine-name">Sauvignon Blanc</h2>
      <p class="abv">Alc. 12.5% by Vol.</p>
      <p class="region">Palos Verdes Peninsula</p>
      <p class="vintage">• YEAR 2022 •</p>
    </div>
    <div class="front__band"></div>
  </section>

  <section class="label back back--blanc">
    <div class="back__content">
      <h3 class="warning-title">GOVERNMENT WARNING:</h3>
      <p class="warning-text">(1) According to the Surgeon General, women should not drink alcoholic beverages during pregnancy because of the risk of birth defects.</p>
      <p class="warning-text">(2) Consumption of alcoholic beverages impairs your ability to drive a car or operate machinery, and may cause health problems.</p>
      <p class="sulfites">Contains Sulfates.</p>
      <p class="volume">750ML</p>
      <div class="back-brand"><span class="back-brand__dot"></span>Brindor Ranch</div>
    </div>
  </section>

  <section class="label front front--cab">
    <div class="front__scene" role="img" aria-label="Photograph of a lighthouse with palm trees on red coastal cliffs above the ocean at sunset"></div>
    <div class="front__info">
      <p class="brand-name">Brindor Ranch</p>
      <h2 class="wine-name">Cabernet Sauvignon</h2>
      <p class="abv">Alc. 13.5% by Vol.</p>
      <p class="region">Palos Verdes Peninsula</p>
      <p class="vintage">• YEAR 2022 •</p>
    </div>
    <div class="front__band"></div>
  </section>

  <section class="label back back--cab">
    <div class="back__content">
      <h3 class="warning-title">GOVERNMENT WARNING:</h3>
      <p class="warning-text">(1) According to the Surgeon General, women should not drink alcoholic beverages during pregnancy because of the risk of birth defects.</p>
      <p class="warning-text">(2) Consumption of alcoholic beverages impairs your ability to drive a car or operate machinery, and may cause health problems.</p>
      <p class="sulfites">Contains Sulfates.</p>
      <p class="volume">750ML</p>
      <div class="back-brand"><span class="back-brand__dot"></span>Brindor Ranch</div>
    </div>
  </section>

</body>
</html>
```